YouTube Banner for Psychologist
LiviaNotes
Project: YouTube Banner for Psychologist
Creative Brief
I'm a licensed clinical psychologist with extensive experience. My clients often say "Well Livia Notes...", which caught on. Videos focus on frequent topics in therapy, with useful insights and skills for the general public.
Medical
Anyone interested in personal growth. All ages but probably young adults who are more comfortable with technology. My goal is to create a following that can be monetized at some point.
I want my banner to be bright, professional, and friendly. I like a clean, modern feel. While I use a self-made logo, I'm not very happy with it, so please feel free to be creative and come up with something new! My current YouTube channel: https://www.vidloop.example/@LiviaNotes

```html
<!DOCTYPE html>
<html lang="en">
<head>
<meta charset="UTF-8">
<title>LiviaNotes – Channel Banner</title>
<link rel="stylesheet" href="https://fonts.googleapis.com/css2?family=Oswald:wght@500;700&family=Montserrat:wght@500;700;800&display=swap">
<style>
  :root {
    --royal-blue: #1e3fa6;
    --deep-blue: #16338c;
    --sun-yellow: #f7c51e;
    --ink: #141414;
    --paper: #ffffff;
    --accent-blue: #1d5fae;
  }
  * { margin: 0; padding: 0; box-sizing: border-box; }
  html, body { width: 1200px; height: 432px; overflow: hidden; background: var(--paper); }
  .banner {
    position: relative; width: 1200px; height: 432px; overflow: hidden;
    background: var(--paper); font-family: "Montserrat", Arial, sans-serif;
  }
  .banner__sky {
    position: absolute; left: 0; top: 0; width: 1200px; height: 211px;
    background: var(--royal-blue);
  }
  .banner__stripe {
    position: absolute; left: 0; top: 211px; width: 1200px; height: 18px;
    background: var(--sun-yellow);
  }
  .portrait {
    position: absolute; width: 324px; height: 324px; top: 98px;
    border-radius: 50%; background: var(--sun-yellow);
    display: flex; align-items: center; justify-content: center;
  }
  .portrait--left { left: 84px; }
  .portrait--right { left: 754px; }
  .portrait__photo {
    width: 300px; height: 300px; border-radius: 50%;
    background: radial-gradient(circle at 50% 40%, #8a6a55 0%, #5a4136 35%, var(--deep-blue) 72%);
  }
  .portrait--right .portrait__photo {
    background: radial-gradient(circle at 50% 42%, #9b7763 0%, #3e2e28 38%, #2a4fb8 74%);
  }
  .channel-name {
    position: absolute; left: 0; width: 1200px; top: 36px;
    text-align: center; color: var(--paper);
    font-family: "Montserrat", Arial, sans-serif; font-weight: 800;
    font-size: 46px; line-height: 56px;
  }
  .mic { position: absolute; left: 584px; top: 138px; width: 32px; height: 52px; }
  .pitch {
    position: absolute; left: 0; width: 1200px; top: 238px;
    text-align: center; font-family: "Oswald", Arial, sans-serif;
    color: var(--ink); text-transform: uppercase; font-weight: 700;
  }
  .pitch__intro {
    font-family: "Montserrat", Arial, sans-serif; text-transform: none;
    font-weight: 500; font-size: 15px; line-height: 22px;
  }
  .pitch__line--clinical { font-size: 38px; line-height: 42px; }
  .pitch__line--accent { color: var(--accent-blue); font-size: 40px; line-height: 44px; }
  .pitch__line--small { font-size: 32px; line-height: 36px; }
  .contact { position: absolute; left: 20px; top: 380px; color: var(--ink); }
  .contact__phone {
    display: flex; align-items: center; gap: 8px;
    font-weight: 700; font-size: 18px; line-height: 24px;
  }
  .contact__phone svg { width: 17px; height: 17px; }
  .contact__web { font-size: 12px; font-weight: 500; line-height: 20px; }
  .follow {
    position: absolute; right: 20px; top: 396px;
    display: flex; align-items: center; gap: 8px;
    color: var(--ink); font-size: 14px; font-weight: 700;
  }
  .follow__dot { width: 13px; height: 13px; border-radius: 50%; background: var(--royal-blue); }
  .follow__handle { color: var(--royal-blue); }
</style>
</head>
<body>
<main class="banner">
  <div class="banner__sky"></div>
  <div class="banner__stripe"></div>

  <div class="portrait portrait--left">
    <div class="portrait__photo" role="img" aria-label="Photo of the psychologist smiling and pointing upward toward the channel name"></div>
  </div>
  <div class="portrait portrait--right">
    <div class="portrait__photo" role="img" aria-label="Portrait photo of the psychologist in a dark blazer, smiling"></div>
  </div>

  <h1 class="channel-name">LiviaNotes</h1>

  <svg class="mic" viewBox="0 0 34 56" aria-hidden="true">
    <rect x="9" y="2" width="16" height="30" rx="8" fill="none" stroke="#fff" stroke-width="4"/>
    <path d="M3 24 a14 14 0 0 0 28 0" fill="none" stroke="#fff" stroke-width="4" stroke-linecap="round"/>
    <line x1="17" y1="38" x2="17" y2="50" stroke="#fff" stroke-width="4"/>
    <line x1="9" y1="52" x2="25" y2="52" stroke="#fff" stroke-width="4" stroke-linecap="round"/>
  </svg>

  <section class="pitch">
    <p class="pitch__intro">I'm a Licensed</p>
    <p class="pitch__line pitch__line--clinical">Clinical</p>
    <p class="pitch__line pitch__line--accent">Psychologist</p>
    <p class="pitch__line pitch__line--small">With Extensive</p>
    <p class="pitch__line pitch__line--small">Experience</p>
  </section>

  <div class="contact">
    <p class="contact__phone">
      <svg viewBox="0 0 24 24" aria-hidden="true"><path fill="#141414" d="M6.6 10.8a15.2 15.2 0 0 0 6.6 6.6l2.2-2.2c.3-.3.7-.4 1-.2 1.1.4 2.3.6 3.6.6.6 0 1 .4 1 1V20c0 .6-.4 1-1 1C10.6 21 3 13.4 3 4c0-.6.4-1 1-1h3.5c.6 0 1 .4 1 1 0 1.3.2 2.5.6 3.6.1.3 0 .7-.2 1z"/></svg>
      555-014-2290
    </p>
    <p class="contact__web">www.livianotes.example</p>
  </div>

  <div class="follow">
    <span>Follow us</span>
    <span class="follow__dot"></span>
    <span class="follow__handle">LiviaNotes</span>
  </div>
</main>
</body>
</html>
```